Dental Practice Billboard Design

We are a newer dental practice in need of a simple but appealing billboard for our growing dental practice to attract new patients. The practice is owned by husband and wife dentists and is family friendly in a small town in Kentucky. We try to be very friendly and caring to our patients. Would prefer a blue background for the billboard and our tooth logo to be prominent. We are partial to the Patua One font used in the image below but please feel free to tweak it as you deem necessary. The shape of the uppercase D and lowercase g are why we like that font, so fonts with a similarly shaped “D” and “g” would work as well. Please include our phone number (606) 847-3962. Please see our website Harlowfamilydentistry.com for more info on the practice if needed. Thank you! Looking forward to seeing your creation.
Updates

The dimensions will be 12ft x 24ft (3.6576m x 7.3152m). Apologies for not including this in the original prompt. Thank you all for your submissions.

Industry/Entity Type

Dental

Font styles to use
Other font styles liked:
• Patua One

Colors
0054AA
0677BA
7BADD7
CADEEF
E8F1F8
0094D4
00A9DD
6FCCEA
C7EBF8
E9F6FB
00AB8E
00BBA5
67D7C9
C6EFE9
E9F9F6
59FF00
82FF00
B8FF75
E3FFCB
F4FFEA

Requirements
Must have
• Phone number, website, Logo, Practice name “Harlow Family Dentistry”
Should not have
• A tagline or slogan

```html
<!DOCTYPE html>
<html lang="en">
<head>
<meta charset="utf-8">
<title>Harlow Family Dentistry – Billboard Concepts</title>
<link href="https://fonts.googleapis.com/css2?family=Patua+One&display=swap" rel="stylesheet">
<style>
  :root {
    --stage: #bdbdbd;
    --brand-blue: #2a5aa8;
    --brand-green: #1fb14b;
    --lime: #b9d77b;
    --white: #ffffff;
    --photo-warm: #d9c6a8;
    --photo-light: #f1ece4;
  }
  * { margin: 0; padding: 0; box-sizing: border-box; }
  html, body { width: 1200px; height: 1200px; overflow: hidden; }
  body {
    background: var(--stage);
    font-family: "Patua One", Georgia, serif;
    position: relative;
  }
  .billboard {
    position: absolute;
    left: 68px;
    width: 1061px;
    height: 530px;
    background: var(--brand-blue);
    overflow: hidden;
  }
  .billboard--split { top: 55px; }
  .billboard--full { top: 620px; }
  .billboard__shapes { position: absolute; inset: 0; }
  .text { position: absolute; white-space: nowrap; line-height: 1; }

  /* Concept A */
  .title-a { left: 64px; color: var(--white); }
  .title-a--main { top: 118px; font-size: 76px; }
  .title-a--sub { top: 204px; font-size: 36px; }
  .phone-large { left: 56px; top: 402px; color: var(--lime); font-size: 48px; }
  .site-a { left: 61px; top: 462px; color: var(--white); font-size: 24px; }

  .name-mark { display: flex; align-items: center; gap: 10px; position: absolute; white-space: nowrap; }
  .name-mark__dot { width: 20px; height: 20px; border-radius: 50%; background: var(--brand-green); flex: none; }
  .name-mark__text { font-size: 22px; line-height: 1.15; }
  .name-mark--a { left: 845px; top: 244px; color: var(--brand-blue); }
  .name-mark--b { left: 862px; top: 80px; color: var(--white); }

  /* Concept B */
  .practice-name { left: 0; width: 448px; text-align: center; color: var(--white); }
  .practice-name--main { top: 150px; font-size: 82px; }
  .practice-name--sub { top: 244px; font-size: 36px; }
  .rule { position: absolute; left: 189px; top: 312px; width: 71px; height: 2px; background: var(--white); }
  .site-b { left: 0; width: 448px; top: 340px; text-align: center; color: var(--white); font-size: 19px; }
  .phone-pill {
    position: absolute; left: 727px; top: 402px; width: 298px; height: 62px;
    border-radius: 31px; background: var(--brand-green);
    display: flex; align-items: center; gap: 14px; padding-left: 18px;
    color: var(--white); font-size: 34px; white-space: nowrap;
  }
  .phone-pill svg { flex: none; }
</style>
</head>
<body>

<section class="billboard billboard--split">
  <svg class="billboard__shapes" width="1061" height="530" viewBox="0 0 1061 530">
    <defs>
      <linearGradient id="photoToneA" x1="0" y1="0" x2="1" y2="1">
        <stop offset="0" stop-color="#d9c6a8"/>
        <stop offset="1" stop-color="#f1ece4"/>
      </linearGradient>
    </defs>
    <polygon points="787,0 1061,0 1061,530 645,530" fill="#ffffff"/>
    <rect x="410" y="70" width="360" height="440" rx="48" fill="url(#photoToneA)" role="img" aria-label="Photo of the two dentists in white coats, smiling outside the practice"/>
  </svg>
  <p class="text title-a title-a--main">Harlow</p>
  <p class="text title-a title-a--sub">Family Dentistry</p>
  <p class="text phone-large">(606) 847-3962</p>
  <p class="text site-a">Harlowfamilydentistry.com</p>
  <div class="name-mark name-mark--a">
    <span class="name-mark__dot"></span>
    <span class="name-mark__text">Harlow<br>Family Dentistry</span>
  </div>
</section>

<section class="billboard billboard--full">
  <svg class="billboard__shapes" width="1061" height="530" viewBox="0 0 1061 530">
    <defs>
      <linearGradient id="photoToneB" x1="0" y1="0" x2="1" y2="1">
        <stop offset="0" stop-color="#d9c6a8"/>
        <stop offset="1" stop-color="#f1ece4"/>
      </linearGradient>
    </defs>
    <rect x="400" y="40" width="362" height="452" rx="48" fill="url(#photoToneB)" role="img" aria-label="Photo of the two dentists in white coats, smiling outside the practice"/>
  </svg>
  <p class="text practice-name practice-name--main">Harlow</p>
  <p class="text practice-name practice-name--sub">Family Dentistry</p>
  <span class="rule"></span>
  <p class="text site-b">Harlowfamilydentistry.com</p>
  <div class="name-mark name-mark--b">
    <span class="name-mark__dot"></span>
    <span class="name-mark__text">Harlow<br>Family Dentistry</span>
  </div>
  <div class="phone-pill">
    <svg width="30" height="30" viewBox="0 0 24 24" aria-hidden="true">
      <path fill="#1a5a8a" d="M6.6 10.8a15.1 15.1 0 0 0 6.6 6.6l2.2-2.2a1 1 0 0 1 1-.25 11.4 11.4 0 0 0 3.6.57 1 1 0 0 1 1 1V20a1 1 0 0 1-1 1A17 17 0 0 1 3 4a1 1 0 0 1 1-1h3.5a1 1 0 0 1 1 1c0 1.25.2 2.450.57 3.6a1 1 0 0 1-.25 1z"/>
    </svg>
    <span>(606) 847-3962</span>
  </div>
</section>

</body>
</html>
```